stationary for a modern hotel
Venmiro Hotels
Project: stationary for a modern hotel
stationary for a modern hotel - Hospitality Industry
Creative Brief
Use same font as used in my logo
anything that can go very well with my logo
Simple
Tundeyemi Okafordike
G.M
Venmiro Hotels Plot 318,Adebanjo-Ekwueme Way,Garki District Abuja Nigeria
tunde@venmirohotels.com
www.venmirohotels.com

```html
<!DOCTYPE html>
<html lang="en">
<head>
<meta charset="utf-8">
<title>Venmiro Hotels – Business Card</title>
<link rel="stylesheet" href="https://fonts.googleapis.com/css2?family=Open+Sans:wght@400;600&display=swap">
<style>
  :root{
    --page-bg:#d9d6d2;
    --card-frost:#eeebe7;
    --card-frost-edge:#f7f5f2;
    --brand-brown:#a57c52;
    --brand-dark:#6b4220;
    --brand-silver:#d8d4cf;
    --brand-name:#a88058;
    --text-light:#ffffff;
  }
  *{margin:0;padding:0;box-sizing:border-box}
  html,body{width:1200px;height:755px;overflow:hidden;background:var(--page-bg)}
  .canvas{position:relative;width:1200px;height:755px}
  .card{
    position:absolute;left:80px;top:76px;width:1040px;height:602px;
    border-radius:34px;overflow:hidden;
    background:linear-gradient(180deg,var(--card-frost-edge),var(--card-frost));
    box-shadow:0 6px 24px rgba(0,0,0,.12);
  }
  .card-waves{position:absolute;inset:0;width:100%;height:100%}
  .brand{
    position:absolute;left:56px;top:120px;width:360px;text-align:center;
    font-family:"Open Sans",sans-serif;font-weight:400;font-size:38px;
    line-height:1;white-space:nowrap;color:var(--brand-name);letter-spacing:.5px;
  }
  .contact{
    position:absolute;left:48px;top:378px;
    font-family:"Open Sans",sans-serif;font-size:15px;line-height:26px;color:var(--text-light);
    list-style:none;
  }
  .contact li{display:flex;align-items:center;gap:10px;white-space:nowrap}
  .icon{width:15px;height:15px;flex:none}
  .holder{
    position:absolute;right:44px;top:505px;text-align:right;
    font-family:"Open Sans",sans-serif;color:var(--text-light);
  }
  .holder-name{font-size:19px;font-weight:600;line-height:26px}
  .holder-role{font-size:15px;line-height:22px}
</style>
</head>
<body>
<div class="canvas">
  <div class="card">
    <svg class="card-waves" viewBox="0 0 1040 602" preserveAspectRatio="none" aria-hidden="true">
      <path d="M0,300 C250,285 520,330 760,430 C880,480 980,420 1040,360 L1040,602 L0,602 Z" fill="var(--brand-brown)"/>
      <path d="M0,275 C260,270 560,330 780,430 C900,480 990,400 1040,330 L1040,360 C980,430 880,470 760,415 C540,320 260,290 0,300 Z" fill="var(--brand-dark)"/>
      <path d="M0,310 C300,300 560,360 780,460 C900,510 990,440 1040,380 L1040,400 C990,455 900,530 770,475 C560,380 300,325 0,330 Z" fill="var(--brand-silver)"/>
    </svg>

    <div class="brand">VENMIRO HOTELS</div>

    <ul class="contact">
      <li>Venmiro Hotels</li>
      <li>Plot 318,Adebanjo-Ekwueme Way,</li>
      <li>Garki District Abuja Nigeria</li>
      <li><svg class="icon" viewBox="0 0 14 14"><circle cx="7" cy="7" r="7" fill="#fff"/><path d="M4.5 3.5l1.5 0 .6 1.8-1 .8a5 5 0 0 0 2.3 2.3l.8-1 1.8.6v1.5c0 .5-.5.9-1 .8A6.5 6.5 0 0 1 3.7 4.5c-.1-.5.3-1 .8-1z" fill="var(--brand-brown)"/></svg>+2348105550142</li>
      <li><svg class="icon" viewBox="0 0 14 14"><circle cx="7" cy="7" r="7" fill="#fff"/><path d="M4.5 3.5l1.5 0 .6 1.8-1 .8a5 5 0 0 0 2.3 2.3l.8-1 1.8.6v1.5c0 .5-.5.9-1 .8A6.5 6.5 0 0 1 3.7 4.5c-.1-.5.3-1 .8-1z" fill="var(--brand-brown)"/></svg>+2348105550187</li>
      <li><svg class="icon" viewBox="0 0 14 14"><circle cx="7" cy="7" r="7" fill="#fff"/><rect x="3.5" y="4.5" width="7" height="5" fill="none" stroke="var(--brand-brown)" stroke-width="1"/><path d="M3.5 4.5L7 7.3 10.5 4.5" fill="none" stroke="var(--brand-brown)" stroke-width="1"/></svg>tunde@venmirohotels.com</li>
      <li><svg class="icon" viewBox="0 0 14 14"><circle cx="7" cy="7" r="7" fill="#fff"/><circle cx="7" cy="7" r="3.6" fill="none" stroke="var(--brand-brown)" stroke-width="1"/><path d="M3.4 7h7.2M7 3.4v7.2" stroke="var(--brand-brown)" stroke-width="1"/></svg>www.venmirohotels.com</li>
    </ul>

    <div class="holder">
      <div class="holder-name">Tundeyemi Okafordike</div>
      <div class="holder-role">G.M</div>
    </div>
  </div>
</div>
</body>
</html>
```